Twelve Weeks of Hope Greater Boston

Need graphic design by 8 a.m. Sun January 12 2020.

Logo Text

Stand Tall Twelve Weeks of Hope for Greater Boston January 12-31 2020

Colors

Designer to choose colors to be used in the design.

```html
<!DOCTYPE html>
<html lang="en">
<head>
<meta charset="utf-8">
<title>Twelve Weeks of Hope for Greater Boston</title>
<link rel="stylesheet" href="https://fonts.googleapis.com/css2?family=Kaushan+Script&family=Poppins:wght@500;600;700&display=swap">
<style>
  :root {
    --page: #ffffff;
    --panel: #050505;
    --ink-light: #ffffff;
    --gold-top: #ffc21a;
    --gold-bottom: #e58a00;
    --sky-deep: #0d1a26;
    --sky-mid: #1c2e3f;
    --hands-warm: #3a2a1e;
  }
  html, body {
    margin: 0;
    padding: 0;
    width: 1000px;
    height: 1200px;
    overflow: hidden;
    background: var(--page);
  }
  .poster {
    position: absolute;
    left: 57px;
    top: 286px;
    width: 886px;
    height: 626px;
    background: var(--panel);
  }
  .poster svg { display: block; }
  .script-word {
    font-family: "Kaushan Script", cursive;
    fill: url(#gold);
  }
  .count {
    font-family: "Poppins", sans-serif;
    font-weight: 700;
    font-size: 78px;
    fill: var(--ink-light);
  }
  .lead {
    font-family: "Poppins", sans-serif;
    font-weight: 500;
    font-size: 35px;
    fill: var(--ink-light);
  }
  .region {
    font-family: "Poppins", sans-serif;
    font-weight: 600;
    font-size: 47px;
    fill: url(#gold);
  }
  .dates {
    font-family: "Poppins", sans-serif;
    font-weight: 500;
    font-size: 28px;
    fill: var(--ink-light);
  }
</style>
</head>
<body>
  <div class="poster">
    <svg width="886" height="626" viewBox="0 0 886 626" xmlns="http://www.w3.org/2000/svg">
      <defs>
        <linearGradient id="gold" x1="0" y1="0" x2="0" y2="1">
          <stop offset="0" stop-color="var(--gold-top)"/>
          <stop offset="1" stop-color="var(--gold-bottom)"/>
        </linearGradient>
        <linearGradient id="skyline-tone" x1="0" y1="0" x2="0" y2="1">
          <stop offset="0" stop-color="var(--panel)" stop-opacity="0"/>
          <stop offset="0.3" stop-color="var(--sky-deep)"/>
          <stop offset="0.7" stop-color="var(--sky-mid)"/>
          <stop offset="1" stop-color="var(--panel)" stop-opacity="0"/>
        </linearGradient>
        <radialGradient id="hands-tone" cx="0.55" cy="0.6" r="0.55">
          <stop offset="0" stop-color="var(--hands-warm)"/>
          <stop offset="1" stop-color="var(--panel)" stop-opacity="0"/>
        </radialGradient>
      </defs>

      <rect class="skyline-photo" x="0" y="80" width="886" height="290" fill="url(#skyline-tone)" role="img" aria-label="Photo of the Boston city skyline at dusk"/>
      <rect class="prayer-photo" x="220" y="390" width="540" height="236" fill="url(#hands-tone)" role="img" aria-label="Photo of folded hands resting on an open Bible"/>

      <text class="script-word" x="448" y="124" text-anchor="middle" font-size="130">Stand</text>

      <text x="691" y="267" text-anchor="end"><tspan class="count">Twelve</tspan><tspan class="lead" dx="10">Weeks of Hope for</tspan></text>
      <text class="region" x="691" y="327" text-anchor="end">Greater Boston</text>
      <text class="dates" x="688" y="381" text-anchor="end">January 12-31 2020</text>

      <text class="script-word" x="443" y="548" text-anchor="middle" font-size="140">Tall</text>
    </svg>
  </div>
</body>
</html>
```